Its a flyer to a course entitled :
Ultrasound Course

Basically we teach students about the use of ultrasound for very sick patients

-I need a title in 3D
-I need an attractive design please
something extraordinary

Please if you have any ongoing project let me know Thanks

Dear Designers Was looking for something new that I did not see before, unfortunately did not find that yet! To clarify the idea, remember the T.V series 'KJ'.. so we have a sick patient like the one you have seen in the series and now we are using Ultrasound to help get the diagnosis and even it helps us in the procedures so basically will use the ultrasound to help saving those patients and give them the treatment in a short time.j

```html
<!DOCTYPE html>
<html lang="en">
<head>
<meta charset="utf-8">
<title>Ultrasound Course Postcard</title>
<link href="https://fonts.googleapis.com/css2?family=Teko:wght@400;500&family=Lato:wght@400;700&family=Archivo+Narrow:wght@700&display=swap" rel="stylesheet">
<style>
  :root {
    --purple: #3a1f6b;
    --blue: #36a3da;
    --blue-text: #2e9fd8;
    --white: #ffffff;
    --ink: #333333;
    --stage: #e6e3df;
    --photo-dark: #2a2116;
    --photo-mid: #8a7150;
    --photo-light: #c9b48f;
  }
  * { margin: 0; padding: 0; box-sizing: border-box; }
  html, body { width: 765px; height: 1200px; overflow: hidden; }
  body { background: var(--stage); position: relative; font-family: "Lato", sans-serif; }

  .postcard { position: absolute; overflow: hidden; background: var(--white); box-shadow: 0 4px 14px rgba(0,0,0,.25); }
  .postcard svg.shapes { position: absolute; inset: 0; }
  .postcard .text { position: absolute; }

  .front { left: 40px; top: 50px; width: 670px; height: 510px; }
  .back { left: 40px; top: 630px; width: 665px; height: 510px; }

  .front-title {
    right: 16px; top: 30px; width: 380px; text-align: right;
    font-family: "Archivo Narrow", sans-serif; font-weight: 700;
    font-size: 34px; line-height: 38px; color: var(--white);
    text-shadow: 1px 2px 0 rgba(0,0,0,.35), 2px 4px 4px rgba(0,0,0,.4);
  }
  .panel-heading {
    left: 30px; top: 165px; width: 215px;
    font-family: "Teko", sans-serif; font-weight: 500; font-size: 17px; line-height: 22px;
    color: var(--white); text-transform: uppercase; letter-spacing: .2px;
  }
  .panel-note {
    left: 34px; width: 160px; font-size: 9.2px; line-height: 14px; color: var(--white);
  }
  .panel-note.first { top: 268px; }
  .panel-note.second { top: 364px; }

  .feature-heading {
    left: 290px; top: 343px; width: 365px;
    font-family: "Teko", sans-serif; font-weight: 500; font-size: 19px; line-height: 20px;
    color: var(--blue-text); text-transform: uppercase;
  }
  .feature-body {
    left: 290px; top: 389px; width: 348px; font-size: 13.4px; line-height: 16.5px; color: var(--ink);
  }
  .phone {
    left: 40px; top: 464px; display: flex; align-items: center; gap: 10px;
    font-family: "Teko", sans-serif; font-weight: 500; font-size: 32px; line-height: 1; color: var(--white);
  }

  .back-heading {
    left: 25px; top: 34px; width: 320px;
    font-family: "Teko", sans-serif; font-weight: 500; font-size: 16.5px; line-height: 20px;
    color: var(--white); text-transform: uppercase;
  }
  .back-body {
    left: 25px; top: 156px; width: 292px; font-size: 16px; line-height: 20.5px; color: var(--white);
  }
  .back-body p + p { margin-top: 10px; }
  .website {
    left: 68px; top: 382px; display: flex; align-items: center; gap: 10px;
    font-weight: 700; font-size: 21px; color: var(--white); white-space: nowrap;
  }
</style>
</head>
<body>

<section class="postcard front">
  <svg class="shapes" width="670" height="510" viewBox="0 0 670 510">
    <defs>
      <radialGradient id="scanTone" cx="0.45" cy="0.55" r="0.7">
        <stop offset="0" stop-color="var(--photo-light)"/>
        <stop offset="0.5" stop-color="var(--photo-mid)"/>
        <stop offset="1" stop-color="var(--photo-dark)"/>
      </radialGradient>
      <linearGradient id="deviceTone" x1="0" y1="0" x2="1" y2="1">
        <stop offset="0" stop-color="#d7d9dc"/>
        <stop offset="1" stop-color="#4b4f57"/>
      </linearGradient>
    </defs>
    <rect width="670" height="310" fill="url(#scanTone)" role="img" aria-label="Sepia ultrasound scan image"/>
    <path d="M0,180 C150,200 300,230 400,270 C500,305 600,290 670,250 L670,510 L0,510Z" fill="var(--purple)"/>
    <path d="M0,230 C200,240 350,300 470,318 C560,332 620,300 670,272 L670,510 L0,510Z" fill="var(--blue)"/>
    <path d="M0,272 C200,282 350,335 470,343 C560,348 630,312 670,292 L670,470 L0,470Z" fill="var(--white)"/>
    <path d="M0,455 L320,455 C450,482 560,472 670,438 L670,510 L0,510Z" fill="var(--purple)"/>
    <path d="M330,470 C450,490 570,480 670,448" fill="none" stroke="var(--blue)" stroke-width="5"/>
    <path d="M15,112 C80,104 170,100 250,70 L250,455 L15,455Z" fill="var(--blue)" stroke="var(--white)" stroke-width="3"/>
    <line x1="34" y1="245" x2="215" y2="245" stroke="rgba(255,255,255,.5)"/>
    <line x1="34" y1="345" x2="215" y2="345" stroke="rgba(255,255,255,.5)"/>
    <circle cx="246" cy="292" r="38" fill="url(#deviceTone)" stroke="var(--white)" stroke-width="4" role="img" aria-label="Photo of an ultrasound probe on a patient"/>
    <circle cx="246" cy="392" r="38" fill="url(#scanTone)" stroke="var(--white)" stroke-width="4" role="img" aria-label="Ultrasound scan detail"/>
  </svg>

  <h1 class="text front-title">Ultrasound Course<br>for the critically<br>ill patient</h1>
  <p class="text panel-heading">Lorem Ipsum is simply dummy text of the printing and typesetting industry. Lorem Ipsum has been the industry's standard dummy</p>
  <p class="text panel-note first">Lorem Ipsum is simply dummy text of the printing and typesetting industry. Lorem Ipsum has been the industry's standard</p>
  <p class="text panel-note second">Lorem Ipsum is simply dummy text of the printing and typesetting industry. Lorem Ipsum has been the industry's standard</p>
  <h2 class="text feature-heading">Lorem Ipsum is simply dummy text of the printing and typesetting industry.</h2>
  <p class="text feature-body">Lorem Ipsum is simply dummy text of the printing and typesetting industry. Lorem Ipsum has been the industry's standard dummy text ever since the 1500s, Lorem Ipsum is simply dummy text of the printing and</p>
  <div class="text phone">
    <svg width="22" height="22" viewBox="0 0 22 22" aria-hidden="true">
      <rect width="22" height="22" rx="4" fill="var(--white)"/>
      <path d="M7,4 L9.5,4 L10.5,8 L8.8,9.3 C9.6,11 11,12.4 12.7,13.2 L14,11.5 L18,12.5 L18,15 C18,16.2 17,17 15.8,17 C10,16.6 5.4,12 5,6.2 C5,5 5.8,4 7,4Z" fill="var(--purple)"/>
    </svg>
    <span>555-014-220</span>
  </div>
</section>

<section class="postcard back">
  <svg class="shapes" width="665" height="510" viewBox="0 0 665 510">
    <rect x="0" y="0" width="350" height="440" fill="var(--purple)"/>
    <path d="M0,128 C120,152 230,82 350,96 L350,328 C230,312 120,372 0,342Z" fill="var(--blue)" stroke="var(--white)" stroke-width="4"/>
    <path d="M0,445 C150,405 350,432 450,446 C550,458 620,442 665,420 L665,510 L0,510Z" fill="var(--blue)" stroke="var(--white)" stroke-width="4"/>
    <rect x="531" y="40" width="91" height="91" fill="none" stroke="#222" stroke-width="1.5"/>
    <line x1="378" y1="157" x2="650" y2="157" stroke="#444" stroke-width="1.2"/>
    <line x1="378" y1="188" x2="650" y2="188" stroke="#444" stroke-width="1.2"/>
    <line x1="378" y1="221" x2="650" y2="221" stroke="#444" stroke-width="1.2"/>
  </svg>

  <p class="text back-heading">Lorem Ipsum is simply dummy text of the printing and typesetting industry. Lorem Ipsum has been the industry's standard dummy text ever since the 1500s,</p>
  <div class="text back-body">
    <p>Lorem Ipsum is simply dummy text of the printing and typesetting industry. Lorem Ipsum has been the industry's standard dummy text ever since the 1500s,</p>
    <p>Lorem Ipsum is simply dummy text of the printing and typesetting industry.</p>
  </div>
  <div class="text website">
    <svg width="24" height="16" viewBox="0 0 24 16" aria-hidden="true">
      <rect x="1" y="1" width="22" height="14" fill="var(--white)"/>
      <path d="M1,1 L12,9 L23,1" fill="none" stroke="var(--purple)" stroke-width="1.6"/>
    </svg>
    <span>www.sonx.com</span>
  </div>
</section>

</body>
</html>
```